Envelope Design - Winner can do follow-up business

- Varindo.com is a Swiss-based online store selling business shirts and accessories for business men
- Please visit the webpage to make yourself familiar with the company. Although the text is in German, with Google translator you should be able to understand the main content.
- Our clients are mainly business men between 30 and 60 years old. Mostly with a high income working in the service industry (banking, insurance, lawyers, etc.). Sometimes there wives purchase the shirts for them ;-)
- The colors and the logo are given, as they are also used for the print materials (please see files in attachment)
- I am running several businesses and often need a talented web designer --> the winner gets substantial follow-up business
your task:
-for our company we need a new envelope design
-It should be simple and modern
-please use one of the logos in the followings.
-suprise me :)

```html
<!DOCTYPE html>
<html lang="en">
<head>
<meta charset="utf-8">
<title>Varindo Envelope Set</title>
<link href="https://fonts.googleapis.com/css2?family=Open+Sans:wght@400;600&display=swap" rel="stylesheet">
<style>
  :root {
    --backdrop: #ece9e4;
    --paper: #ffffff;
    --edge: #c9c9c9;
    --brand-red: #ee2e24;
    --brand-yellow: #e6d76a;
    --ink: #1c1c1c;
  }
  * { margin: 0; padding: 0; box-sizing: border-box; }
  html, body {
    width: 1200px; height: 961px; overflow: hidden;
    background: var(--backdrop);
    font-family: "Open Sans", Arial, sans-serif;
  }
  .stage { position: relative; width: 1200px; height: 961px; }
  .envelope {
    position: absolute; width: 975px; height: 459px;
    background: var(--paper); border: 1px solid var(--edge);
  }
  .envelope--back { left: 163px; top: 35px; }
  .envelope--middle { left: 70px; top: 224px; }
  .envelope--front { left: 38px; top: 457px; }
  .flap { position: absolute; left: 0; top: 0; width: 975px; height: 160px; }
  .flap-name {
    position: absolute; left: 0; top: 46px; width: 975px; text-align: center;
    font-weight: 600; font-size: 42px; letter-spacing: 3px; color: var(--brand-yellow);
  }
  .brand-block { position: absolute; left: 62px; top: 28px; }
  .brand-square {
    width: 46px; height: 46px; margin-left: 127px; background: var(--brand-red);
  }
  .brand-name {
    margin-top: 26px; font-weight: 600; font-size: 46px; letter-spacing: 4px;
    line-height: 1; color: var(--brand-yellow);
  }
  .contact { position: absolute; left: 26px; top: 360px; font-size: 19px; color: var(--ink); }
  .contact-row { display: flex; align-items: center; height: 36px; }
  .contact-row svg { width: 24px; height: 24px; margin-right: 12px; }
  .contact-row--web { margin-left: 36px; }
  .contact-row--web svg { margin-right: 10px; }
  .footer-bands { position: absolute; left: 0; bottom: 0; width: 975px; height: 46px; }
</style>
</head>
<body>
<div class="stage">

  <div class="envelope envelope--back">
    <svg class="flap" viewBox="0 0 975 160" aria-hidden="true">
      <path d="M0 0 H975 C965 30 955 52 895 64 L520 150 Q487 157 455 150 L80 64 C20 52 10 30 0 0 Z" fill="var(--brand-red)"/>
    </svg>
    <div class="flap-name">VARINDO</div>
  </div>

  <div class="envelope envelope--middle">
    <svg class="flap" viewBox="0 0 975 160" aria-hidden="true">
      <path d="M0 0 H975 C965 30 955 52 895 64 L520 150 Q487 157 455 150 L80 64 C20 52 10 30 0 0 Z" fill="var(--brand-yellow)"/>
    </svg>
  </div>

  <div class="envelope envelope--front">
    <div class="brand-block">
      <div class="brand-square"></div>
      <div class="brand-name">VARINDO</div>
    </div>

    <div class="contact">
      <div class="contact-row contact-row--web">
        <svg viewBox="0 0 24 24" aria-hidden="true" fill="none" stroke="var(--brand-red)" stroke-width="1.6">
          <circle cx="12" cy="12" r="10"/>
          <ellipse cx="12" cy="12" rx="4.5" ry="10"/>
          <path d="M2 12 H22 M4 7 H20 M4 17 H20"/>
        </svg>
        <span>www.varindo.com</span>
      </div>
      <div class="contact-row">
        <svg viewBox="0 0 24 24" aria-hidden="true">
          <path d="M12 1 C7 1 4 4.6 4 9 C4 14.5 12 23 12 23 C12 23 20 14.5 20 9 C20 4.6 17 1 12 1 Z" fill="var(--brand-red)"/>
          <circle cx="12" cy="9" r="3.2" fill="var(--paper)"/>
        </svg>
        <span>Street Name, City Name, State Zipcode</span>
      </div>
    </div>

    <svg class="footer-bands" viewBox="0 0 975 46" aria-hidden="true">
      <polygon points="0,25 502,25 481,46 0,46" fill="var(--brand-yellow)"/>
      <polygon points="544,0 975,0 975,46 487,46" fill="var(--brand-red)"/>
    </svg>
  </div>

</div>
</body>
</html>
```